practice letterhead

I need a letterhead design for a new company that is a veterinary specialty company. I am conservative. I want it to look professional - not "cutesy"

I need my name, credentials, address, phone number and website/email on it.

My personal information is as follows: Marisol Tedder, DVM, DACVIM (Neurology) Certified Veterinary Pain Practitioner (or CVPP) Certified Canine Rehabilitation Therapist (or CCRT) 4170 Larkfield Hwy Brookhaven, MA 01794 508-347-6620 marisol.tedder@petspineandcare.com www.petspineandcare.com

```html
<!DOCTYPE html>
<html lang="en">
<head>
<meta charset="utf-8">
<title>Pet Spine and Care – Letterhead</title>
<link rel="stylesheet" href="https://fonts.googleapis.com/css2?family=Arimo:wght@400;700&display=swap">
<style>
  :root {
    --sage: #6e9186;
    --sage-mid: #9bb5ad;
    --sage-light: #c5d5d0;
    --sage-pale: #e0e8e5;
    --paper: #ffffff;
    --ink-light: #ffffff;
  }
  * { margin: 0; padding: 0; box-sizing: border-box; }
  html, body { width: 848px; height: 1200px; overflow: hidden; background: var(--paper); }
  .letterhead {
    position: relative;
    width: 848px;
    height: 1200px;
    background: var(--paper);
    font-family: "Arimo", Arial, sans-serif;
  }
  .side-mosaic {
    position: absolute;
    left: 20px; top: 18px;
    width: 183px; height: 1165px;
    background: linear-gradient(180deg, var(--sage-light) 0%, var(--sage-mid) 35%, var(--sage-light) 65%, var(--sage-mid) 100%);
  }
  .letter-panel {
    position: absolute;
    left: 222px; top: 18px;
    width: 605px; height: 862px;
    background: var(--sage);
    color: var(--ink-light);
    padding: 50px 57px 0 59px;
    font-size: 16.6px;
    line-height: 25.7px;
  }
  .letter-panel p { text-align: justify; margin-bottom: 25.7px; }
  .footer-rule {
    position: absolute;
    left: 222px; top: 917px;
    width: 605px; height: 0;
    border-top: 1.5px solid var(--sage);
  }
  .sender {
    position: absolute;
    right: 21px; top: 947px;
    text-align: right;
    color: var(--sage);
    font-style: normal;
    font-size: 17px;
    line-height: 19.5px;
    white-space: nowrap;
  }
  .practice-mark {
    position: absolute;
    right: 20px; top: 1117px;
    display: flex;
    align-items: center;
    gap: 14px;
    color: var(--sage);
    font-weight: 700;
    font-size: 17px;
    line-height: 21px;
  }
  .practice-mark .dot {
    width: 58px; height: 58px;
    border-radius: 50%;
    background: var(--sage);
  }
  .practice-mark .name { text-align: left; }
</style>
</head>
<body>
  <main class="letterhead">
    <div class="side-mosaic" role="img" aria-label="Column of soft sage-toned mosaic squares"></div>

    <section class="letter-panel">
      <p>Lorem ipsum,</p>
      <p>Lorem ipsum dolor sit amet, consectetur adipiscing elit. Maecenas ullamcorper laoreet augue, vel eleifend tellus eleifend sed. Phasellus in posuere mi. Mauris vitae vulputate erat. Integer quis facilisis dui. Nunc aliquam posuere turpis id venenatis. Donec bibendum vel augue et cursus. Fusce egestas malesuada dictum.</p>
      <p>Ut augue sem, lacinia id arcu vel, fringilla sodales sem. Pellentesque pellentesque dui erat, at vulputate mauris blandit id. Sed euismod sit amet lacus ut dictum. Vivamus malesuada sodales enim, id tristique turpis faucibus vel. Maecenas vitae dapibus sem. Maecenas dui tortor, tincidunt id lobortis non, fringilla in elit. Phasellus cursus urna sed hendrerit luctus. Pellentesque tempus urna sed nibh suscipit, sed iaculis leo malesuada. Nam tellus purus, sagittis ac sodales sit amet, suscipit non massa.</p>
      <p>Mauris ac vestibulum nisi. Donec molestie dignissim dui, at tristique eros. Sed elit enim, mattis quis odio in, congue ultrices tellus. Nam feugiat massa vel dui rhoncus tristique. Vestibulum tempor velit dignissim, volutpat magna nec, scelerisque nisi. Mauris tellus leo, interdum id urna eget, rhoncus fringilla tellus. Sed ut ultricies augue. Donec faucibus mi sit amet dui rhoncus, eu placerat ipsum aliquet. Donec gravida tristique massa id rutrum. Fusce non malesuada sapien. In varius metus laoreet, iaculis tortor ultrices, viverra ante.</p>
      <p>Quisque vel pharetra odio. Aliquam euismod auctor commodo. Aliquam nec justo ut sem dictum ullamcorper quis eu sem. Lorem ipsum dolor sit amet, consectetur adipiscing elit.</p>
    </section>

    <div class="footer-rule"></div>

    <address class="sender">
      Marisol Tedder, DVM, DACVIM (Neurology) Certified Veterinary Pain<br>
      Practitioner, Certified Canine Rehabilitation Therapist<br>
      4170 Larkfield Hwy Brookhaven, MA;<br>
      01794 508-347-6620<br>
      marisol.tedder@petspineandcare.com<br>
      www.petspineandcare.com
    </address>

    <div class="practice-mark">
      <span class="dot"></span>
      <span class="name">Pet Spine and Care<br>Veterinary Specialty Clinic</span>
    </div>
  </main>
</body>
</html>
```